Our new beauty salon requires a price list brochure

Our beauty clinic is a medical grade skin care clinic. So our salon is very clinical and professional in appearance. I would like the colours to be similar to our logo design with some nice texture or abstract shapes thrown in.
Pricelist, contact details and logo is attached
I would prefer it to be a 3 fold brochure.

Target Market(s)

Females aged 30-50

Colors
85acd3
cedeed
c4c4c4
5c5c5c
000000
ffffff
eea3c7
f9d9e8
dbdbdb

Requirements
Must have
• easy to read

```html
<!DOCTYPE html>
<html lang="en">
<head>
<meta charset="utf-8">
<title>Willow Aesthetics – Price List Brochure</title>
<link rel="stylesheet" href="https://fonts.googleapis.com/css2?family=Raleway:wght@300;400;500&family=Yellowtail&display=swap">
<style>
  :root {
    --ink: #000000;
    --panel: #0b0b0c;
    --band: #161718;
    --ring: #2a2d31;
    --blue: #85acd3;
    --blue-pale: #cedeed;
    --grey: #c4c4c4;
    --grey-dark: #5c5c5c;
    --logo-grey: #6f7f90;
    --white: #ffffff;
    --skin: #e9c3a8;
    --stage: #e6e6e6;
  }
  * { margin: 0; padding: 0; box-sizing: border-box; }
  html, body { width: 1200px; height: 1038px; overflow: hidden; background: var(--stage); }
  .brochure {
    position: relative; width: 1200px; height: 1038px; overflow: hidden;
    background: linear-gradient(180deg, #101112 0%, var(--panel) 60%, #050505 100%);
    font-family: "Raleway", sans-serif; color: var(--white);
  }
  .decor { position: absolute; inset: 0; }
  .abs { position: absolute; }
  .script { font-family: "Yellowtail", cursive; font-weight: 400; text-align: center; font-size: 24px; line-height: 1.15; color: var(--white); }
  .script .accent, .accent { color: var(--blue); }
  .rule { width: 30px; height: 1px; background: var(--blue); margin: 8px auto 0; }

  /* price panel */
  .price-panel { left: 43px; width: 300px; }
  .price-group { position: absolute; left: 43px; width: 300px; }
  .price-group h2 { font-size: 24px; }
  .price-row { display: flex; justify-content: space-between; font-size: 13.5px; font-weight: 400; line-height: 20px; color: #e8e8e8; }
  .price-row .amount { color: var(--blue); }

  /* about panel */
  .about { left: 424px; width: 334px; font-size: 13.5px; line-height: 20.5px; color: #e6e6e6; }
  .about p { text-align: justify; text-align-last: center; }
  .contact-note { text-align: center; }
  .contact-note .email { color: var(--blue); font-weight: 500; }

  .photo { position: absolute; border-radius: 50%; }
  .brand { text-align: center; font-family: "Raleway", sans-serif; font-weight: 300; color: var(--white); }
  .brand-name { font-size: 34px; letter-spacing: 4px; }
  .brand-name.large { font-size: 50px; color: var(--logo-grey); letter-spacing: 6px; }

  .details { left: 424px; width: 334px; text-align: center; font-size: 12.5px; line-height: 17.5px; }
  .icons { display: flex; justify-content: center; gap: 6px; }
  .socials { display: flex; justify-content: center; align-items: center; gap: 12px; font-size: 13px; }
  .socials span.dot { display: inline-block; width: 13px; height: 13px; border-radius: 50%; background: var(--logo-grey); vertical-align: -2px; margin-right: 8px; }
  .web { font-size: 13px; letter-spacing: 1.5px; color: #dcdcdc; text-align: center; }
</style>
</head>
<body>
<main class="brochure">

  <svg class="decor" width="1200" height="1038" viewBox="0 0 1200 1038">
    <defs>
      <radialGradient id="sparkle" cx="0.3" cy="0.25" r="0.8">
        <stop offset="0" stop-color="#3a3020"/>
        <stop offset="0.5" stop-color="#15161a"/>
        <stop offset="1" stop-color="#0b0b0c"/>
      </radialGradient>
      <linearGradient id="skin" x1="0" y1="0" x2="1" y2="1">
        <stop offset="0" stop-color="#f3d6c2"/>
        <stop offset="1" stop-color="#d9a98c"/>
      </linearGradient>
      <linearGradient id="wave" x1="0" y1="0" x2="0" y2="1">
        <stop offset="0" stop-color="#232427"/>
        <stop offset="1" stop-color="#0c0c0d"/>
      </linearGradient>
    </defs>
    <!-- right panel hero photo area -->
    <rect x="740" y="0" width="460" height="680" fill="url(#sparkle)"/>
    <path role="img" aria-label="Photo of a woman touching her cheek, bare shoulders" d="M 860 0 L 1200 0 L 1200 590 C 1120 630 1010 660 860 650 Z" fill="url(#skin)" opacity="0.9"/>
    <!-- dark wave -->
    <path d="M 400 700 C 560 610 700 600 860 650 C 1000 690 1110 640 1200 590 L 1200 1038 L 400 1038 Z" fill="url(#wave)"/>
    <path d="M 400 700 C 560 610 700 600 860 650 C 1000 690 1110 640 1200 590" fill="none" stroke="#3b3d42" stroke-width="2"/>
    <!-- left circle frame -->
    <circle cx="202" cy="810" r="258" fill="#1c1e21"/>
    <circle cx="202" cy="810" r="232" fill="#8b8f94"/>
    <circle role="img" aria-label="Photo of a smiling woman with hands on her cheeks" cx="195" cy="812" r="222" fill="url(#skin)"/>
    <!-- center circle frame -->
    <circle cx="590" cy="581" r="128" fill="#1e2023"/>
    <circle cx="590" cy="581" r="110" fill="#d0d3d6"/>
    <circle role="img" aria-label="Close-up photo of a woman's eye and lips" cx="590" cy="581" r="104" fill="url(#skin)"/>
    <!-- contact icons -->
    <g fill="#85acd3">
      <circle cx="571" cy="893" r="5.5"/><circle cx="589" cy="893" r="5.5"/><circle cx="607" cy="893" r="5.5"/>
    </g>
    <g fill="#0b0b0c">
      <circle cx="571" cy="892" r="1.8"/>
      <path d="M586.5 890.5 l1.5 -1 l1 2 l-1 1 q1 2 3 3 l1 -1 l2 1 l-1 1.5 q-4 0 -6.5 -6.5z"/>
      <rect x="604" y="890.5" width="6" height="4.5"/>
    </g>
  </svg>

  <!-- left panel: price list -->
  <section class="price-group" style="top:34px">
    <h2 class="script accent">Lumiglow LED</h2>
    <div class="rule"></div>
    <div style="margin-top:18px">
      <div class="price-row"><span>Per treatment or</span><span class="amount">$90</span></div>
      <div class="price-row"><span>When added on to any of our<br>other skin treatments.</span><span class="amount" style="align-self:flex-end">$50</span></div>
    </div>
  </section>

  <section class="price-group" style="top:206px">
    <h2 class="script"><span class="accent">Dermaneedle Microneedling</span><br>(Collagen Induction Therapy)</h2>
    <div class="rule" style="margin-top:18px"></div>
    <div style="margin-top:24px">
      <div class="price-row"><span>Full Face</span><span class="amount">$350</span></div>
      <div class="price-row"><span>Face, Neck and Décolletage</span><span class="amount">$450</span></div>
    </div>
  </section>

  <section class="price-group" style="top:393px">
    <h2 class="script"><span class="accent">Photonix</span> Laser Facial</h2>
    <div class="rule"></div>
    <div style="margin-top:18px">
      <div class="price-row"><span>Full Face</span><span class="amount">$350</span></div>
      <div class="price-row"><span>Face, Neck and Décolletage</span><span class="amount">$450</span></div>
    </div>
  </section>

  <!-- center panel: about -->
  <section class="abs about" style="top:34px">
    <h2 class="script">About <span class="accent">Willow Aesthetics</span></h2>
    <div class="rule"></div>
    <p style="margin-top:14px">General Practitioner Dr Clara Hensley founded Willow Aesthetics in 2015. Dr Clara has a keen interest in skin cancer and cosmetic medicine and has extensive training in these fields. Each individual treatment is tailored to your needs and administered by Dr Clara herself.</p>
    <h2 class="script" style="margin-top:34px">We visit clinics across<br><span class="accent">Perth and also the South-West of WA</span></h2>
    <div class="rule" style="margin-top:12px"></div>
    <p class="contact-note" style="margin-top:16px">Please contact your closest clinic for an appointment or email Dr Clara on<br><span class="email">drclara@willowaesthetics.com.au</span><br>for further information</p>
  </section>

  <div class="abs brand" style="left:424px; width:334px; top:748px">
    <div class="brand-name">willow aesthetics</div>
  </div>

  <section class="abs details" style="top:834px">
    <h2 class="script" style="font-size:22px">Get in Touch with us</h2>
    <div class="rule" style="margin-top:4px"></div>
    <address style="font-style:normal; margin-top:38px">
      4/27 Coastal Road<br>Seabrook Western Australia<br>(08) 9000 4821<br>www.willowaesthetics.com.au
    </address>
    <div class="socials" style="margin-top:24px">
      <span><span class="dot"></span>willow_aesthetics</span>
      <span><span class="dot"></span>willow aesthetics</span>
    </div>
  </section>

  <!-- right panel: cover -->
  <div class="abs brand" style="left:810px; width:380px; top:838px">
    <div class="brand-name large">willow</div>
    <div style="font-size:15px; letter-spacing:14px; color:var(--logo-grey); margin-top:14px">AESTHETICS</div>
  </div>
  <div class="abs web" style="left:810px; width:380px; top:998px">www.willowaesthetics.com.au</div>

</main>
</body>
</html>
```